2 Page Business Flyer for Finance Business

Need a two page flyer created for a finance business. Lots of text and needs to fit on two pages.

Corporate business/banking look and feel. Not too many large images. Lots of white space, clean design. Attached is color palette and the text contents of the flyer.

```html
<!DOCTYPE html>
<html lang="en">
<head>
<meta charset="utf-8">
<title>Vanilla Option Contracts – Two Page Flyer</title>
<link href="https://fonts.googleapis.com/css2?family=Didact+Gothic&family=Mulish:wght@800;900&display=swap" rel="stylesheet">
<style>
  :root{
    --backdrop:#8fa7ae;
    --paper-light:#e0cf9d;
    --paper-dark:#d5c189;
    --red:#c6463d;
    --red-text:#f1c8a8;
    --ink:#35261f;
    --title-ink:#3a1d17;
    --cream:#f4d9b3;
  }
  *{margin:0;padding:0;box-sizing:border-box}
  html,body{width:1200px;height:846px;overflow:hidden;background:var(--backdrop)}
  body{position:relative;font-family:"Didact Gothic",sans-serif;color:var(--ink)}
  .page{
    position:absolute;top:58px;width:515px;height:731px;
    background:linear-gradient(58deg,var(--paper-light) 50%,var(--paper-dark) 50%);
    box-shadow:0 6px 18px rgba(30,50,60,.35);
  }
  .page--left{left:74px}
  .page--right{left:611px}
  .abs{position:absolute}
  p.copy{font-size:11.5px;line-height:14.7px}
  .title-band{left:0;top:21px;width:515px;height:44px;background:var(--red);
    font-family:"Mulish",sans-serif;font-weight:800;font-size:21px;color:var(--cream);
    padding:13px 0 0 26px;letter-spacing:.2px}
  .title-band strong{color:var(--title-ink);font-weight:900}
  .ribbon{background:var(--red);color:var(--red-text);font-size:11.5px;line-height:16px;height:16px;
    clip-path:polygon(0 0,calc(100% - 12px) 0,100% 50%,calc(100% - 12px) 100%,0 100%)}
  .ribbon--step{left:0;width:489px;padding-left:43px}
  .ribbon--both{clip-path:polygon(14px 0,calc(100% - 14px) 0,100% 50%,calc(100% - 14px) 100%,14px 100%,0 50%);
    text-align:center;height:21px;line-height:21px;font-size:12px}
  .ribbon--back{clip-path:polygon(14px 0,100% 0,100% 100%,14px 100%,0 50%);height:19px;line-height:19px;font-size:12.5px;text-align:right;padding-right:30px}
  .ribbon--fwd{height:19px;line-height:19px;font-size:12.5px;padding-left:43px}
  .ribbon .ink{color:var(--title-ink)}
  .section-head{left:0;width:245px;height:21px;background:var(--red);color:var(--ink);
    font-family:"Mulish",sans-serif;font-weight:900;font-size:13px;line-height:21px;padding-left:43px;
    clip-path:polygon(0 0,calc(100% - 14px) 0,100% 50%,calc(100% - 14px) 100%,0 100%)}
  .bullets{left:43px;list-style:none;font-size:11.5px;line-height:17.6px}
</style>
</head>
<body>

<section class="page page--left">
  <h1 class="abs title-band">How does a <strong>Vanilla Option</strong> contract work?</h1>

  <p class="abs copy" style="left:26px;top:74px;width:466px">The buyer of a vanilla option receives protection against an adverse movement in the exchange rate while allowing full participation in a beneficial move. At no time is the buyer of a Vanilla Option obligated to exercise the Option and transact the currencies, therefore providing flexibility in cases where the requirement to purchase foreign currency is not certain.</p>
  <p class="abs copy" style="left:26px;top:154px;width:466px">A buyer of vanilla options is required to pay a premium (like an insurance premium) for the right, but not the obligation, to exchange currency at a predetermined rate on a pre-determined date.</p>

  <div class="abs ribbon ribbon--step" style="top:205px">Set a protection rate which will be your worst-case scenario at expiry</div>
  <div class="abs ribbon ribbon--step" style="top:228px">Determine the amount of currency you wish to protect</div>
  <div class="abs ribbon ribbon--step" style="top:251px">Choose an expiry date for the contract</div>
  <div class="abs ribbon ribbon--step" style="top:275px">Calculate the premium you are required to pay</div>

  <div class="abs ribbon ribbon--both" style="left:78px;top:326px;width:358px;height:19px;line-height:19px">Let’s look at an example &nbsp;⟶ <span class="ink">You are in importer</span></div>

  <p class="abs copy" style="left:26px;top:358px;width:466px">Your construction company has bid on a project that if successful, will require you to import materials from the United States to use in construction. You have used todays pricing of materials in calculating your bid and want to protect against an adverse move in the US dollar exchange rate from eroding your margin if your bid is chosen for the project.</p>
  <p class="abs copy" style="left:26px;top:422px;width:466px">You choose to buy a Vanilla Call which will protect you from a rise in the USD/CAD exchange rate above your protection rate. You choose to buy protection on $500,000 USD, with a protection rate (strike rate) of 1.3300 expiring 3 months from now. You are required to pay a premium which in this case is calculated to be 1.8%, or 11,970 CAD.</p>

  <div class="abs ribbon ribbon--fwd" style="left:0;top:498px;width:246px">YOUR BID IS SUCCESSFUL</div>
  <div class="abs ribbon ribbon--back" style="left:269px;top:498px;width:246px;padding-right:22px">YOUR BID IS NOT SUCCESSFUL</div>

  <p class="abs copy" style="left:26px;top:525px;width:222px">If the exchange rate is below your protection rate at expiration, you have no obligation relating to the vanilla call and you are free to buy USD at the cheaper spot rate. If the exchange rate is above your protection rate, your have the right to purchase your USD at the protection rate, and thereby claiming your insurance policy.</p>
  <p class="abs copy" style="left:270px;top:525px;width:222px;text-align:right">You have no obligation relating to the vanilla option however, if at expiry the exchange rate is above the protection rate, you may exercise your right to buy USD at the lower rate and simultaneous sell USD back at the prevailing spot rate, thereby recouping some or all of the premium paid to buy the option. Alternatively, if you find out your bid was not successful with time still left until expiration, you may sell your option back into the market in the case that it still has residual value, which will depend on various market factors.</p>
</section>

<section class="page page--right">
  <h2 class="abs section-head" style="top:21px">CHARACTERISTICS</h2>
  <ul class="abs bullets" style="top:48px">
    <li>You are looking for a straight-forward hedging solution</li>
    <li>You want to receive full benefit from an appreciation of the currency you are</li>
    <li>You are comfortable receiving protection at the strike rate of the option</li>
    <li>You are willing to pay the non-refundable premium</li>
  </ul>

  <h2 class="abs section-head" style="top:126px">ADVANTAGES</h2>
  <ul class="abs bullets" style="top:153px">
    <li>You hedge your foreign currency exposure at a predefined hedge rate</li>
    <li>You can choose the hedge rate that suits your budget requirements</li>
    <li>Provides the ability to fully participate in a favourable exchange rate move</li>
    <li>You can choose from most major currency pairs to meet your needs</li>
  </ul>

  <h2 class="abs section-head" style="top:232px">RISKS</h2>
  <ul class="abs bullets" style="top:259px">
    <li>Premium paid is non-refundable and remains your only obligation when buying</li>
  </ul>

  <div class="abs ribbon ribbon--both" style="left:133px;top:289px;width:249px">Why use Vanilla Options?</div>
  <p class="abs copy" style="left:26px;top:317px;width:466px">Vanilla options are often compared to an insurance product. The buyer pays a non-refundable premium for the right, but not the obligation to trade currency in the future at the protection rate of the option. This product allows you to participate in a beneficial move to an unlimited extent, which will be the most advantageous outcome, if the exchange rate moves in your favour enough to more than offset the premium paid for the option.</p>

  <div class="abs ribbon ribbon--both" style="left:97px;top:401px;width:321px">What determines the price of a Vanilla Option?</div>
  <p class="abs copy" style="left:26px;top:432px;width:466px">The cost of an option is defined by the premium that is required to be paid in order to enter into the contract. Premiums are calculated using the industry standard formulas based upon the Black Scholes model. The most important variables in the option pricing formulas include the following:</p>

  <div class="abs ribbon ribbon--step" style="top:500px;padding-left:26px">The current market Spot Rate</div>
  <div class="abs ribbon ribbon--step" style="top:523px;padding-left:26px">Market volatility – the higher the volatility, the higher the premium</div>
  <div class="abs ribbon ribbon--step" style="top:547px;padding-left:26px">The Term of the Option – a longer term typically results in a higher premium</div>
  <div class="abs ribbon ribbon--step" style="top:570px;padding-left:26px">The Strike Rate – the closer to being ITM the protection rate is, the higher the premium</div>
  <div class="abs ribbon ribbon--step" style="top:594px;padding-left:26px">The interest rate differential of the two currencies involved</div>
  <div class="abs ribbon ribbon--step" style="top:617px;padding-left:26px">Style – European or American, or whether the option can be exercised prior to expiration</div>

  <p class="abs copy" style="left:26px;top:641px;width:466px">An option can either a European (meaning that they can only be exercised on the expiry date), or American (meaning that they can be exercised at any time prior to expiration). We normally deals in European options however, we do offer American options under certain circumstances and when specific delivery terms are agreed upon between us and the customer.</p>
</section>

</body>
</html>
```